Business Card design for Recruiter providing Recruitment Staff Augmentation services

I need a double sided business card. I have used Zek to print cards in the past and really like their quality. I have a logo but need to change the tagline that is part of the graphic.

The tagline currently reads and Connnecting people with careers - but it should be removed.

The back should look like a notecard for writing a to do list with the first to-do Augment Recruiting Staff

```html
<!DOCTYPE html>
<html lang="en">
<head>
<meta charset="utf-8">
<title>Talent Summit – Business Card</title>
<link rel="stylesheet" href="https://fonts.googleapis.com/css2?family=Lato:wght@400;700&display=swap">
<style>
  :root {
    --navy: #0e3a5c;
    --red: #c9432a;
    --paper: #ffffff;
    --backdrop: #e8ebed;
    --watermark: #e3e6e9;
  }
  * { margin: 0; padding: 0; box-sizing: border-box; }
  html, body {
    width: 1200px; height: 900px; overflow: hidden;
    background: var(--backdrop);
    font-family: "Lato", Arial, sans-serif;
  }
  .sheet {
    width: 1200px; height: 900px;
    display: flex; flex-direction: column; align-items: center; justify-content: center;
    gap: 56px;
  }
  .card {
    position: relative;
    width: 600px; height: 343px;
    background: var(--paper);
    box-shadow: 0 4px 14px rgba(0,0,0,0.12);
    overflow: hidden;
  }
  .card-art { position: absolute; inset: 0; }

  /* Front: plain vertical band along the right edge */
  .edge-rule {
    position: absolute; top: 0; bottom: 0; left: 486px; width: 5px;
    background: var(--red);
  }
  .edge-band {
    position: absolute; top: 0; bottom: 0; left: 500px; right: 0;
    background: var(--navy);
  }
  .front-content { position: absolute; left: 48px; top: 62px; }
  .brand { display: flex; align-items: center; gap: 14px; }
  .brand-dot {
    width: 40px; height: 40px; border-radius: 50%;
    background: var(--red);
  }
  .brand-name {
    font-size: 31px; font-weight: 400; letter-spacing: 2px;
    color: var(--navy); text-transform: uppercase; white-space: nowrap;
  }
  .holder-name {
    margin-top: 40px;
    font-size: 24px; color: var(--red); font-weight: 400;
  }
  .contact {
    margin-top: 12px;
    font-size: 16px; line-height: 1.35; color: var(--navy);
    list-style: none;
  }

  /* Back: lined to-do notecard */
  .watermark {
    position: absolute; left: 0; right: 0; top: 144px;
    text-align: center;
    font-size: 44px; letter-spacing: 3px; text-transform: uppercase;
    color: var(--watermark);
  }
</style>
</head>
<body>
<main class="sheet">

  <section class="card card-front" aria-label="Card front">
    <span class="edge-rule"></span>
    <span class="edge-band"></span>
    <div class="front-content">
      <div class="brand">
        <span class="brand-dot"></span>
        <span class="brand-name">Talent Summit</span>
      </div>
      <p class="holder-name">Dana Whitlow, SPHR</p>
      <ul class="contact">
        <li>303-555-0142</li>
        <li>dana@talentsummit.com</li>
      </ul>
    </div>
  </section>

  <section class="card card-back" aria-label="Card back, lined to-do notecard">
    <span class="watermark">Talent Summit</span>
    <svg class="card-art" viewBox="0 0 600 343" width="600" height="343" aria-hidden="true">
      <line class="rule-top" x1="0" y1="40" x2="600" y2="40" stroke="var(--red)" stroke-width="3"/>
      <g class="rule-lines" stroke="var(--navy)" stroke-width="2">
        <line x1="0" y1="70" x2="600" y2="70"/>
        <line x1="0" y1="100" x2="600" y2="100"/>
        <line x1="0" y1="130" x2="600" y2="130"/>
        <line x1="0" y1="160" x2="600" y2="160"/>
        <line x1="0" y1="190" x2="600" y2="190"/>
        <line x1="0" y1="220" x2="600" y2="220"/>
        <line x1="0" y1="250" x2="600" y2="250"/>
        <line x1="0" y1="280" x2="600" y2="280"/>
        <line x1="0" y1="310" x2="600" y2="310"/>
      </g>
    </svg>
  </section>

</main>
</body>
</html>
```